Quiet Harbor Podcast Business Card Design

Needing a business card with the logo design provided for Quiet Harbor Podcast. I am looking for a modern style that fits the current logo.

Info:
Name: Teodor Vask
Title: Creator/Host
Email: teodor@quietharborcast.com
Phone: (555) 274-9163
www.quietharborcast.com
Twitter: @qharborcast
Instagram: @quietharborcastshow
Facebook: Quiet Harbor Podcast

Industry/Entity Type

Business

Font styles to use
Sans Serif

Colors
000000
ffffff

Requirements
Must have
• modern, clean design
Nice to have
• social media contact info

```html
<!DOCTYPE html>
<html lang="en">
<head>
<meta charset="UTF-8">
<title>Quiet Harbor Podcast — Business Card</title>
<link href="https://fonts.googleapis.com/css2?family=Cabin:wght@400;500;600&display=swap" rel="stylesheet">
<style>
  :root {
    --ink: #000000;
    --paper: #ffffff;
    --card-black: #0d0d0d;
    --card-black-soft: #1c1c1c;
    --silver: #cfcfcf;
    --muted: #b5b5b5;
    --stage: #2a2a2a;
  }
  * { margin: 0; padding: 0; box-sizing: border-box; }
  html, body {
    width: 1200px; height: 1000px; overflow: hidden;
    background: var(--stage);
    font-family: "Cabin", "Gill Sans", sans-serif;
  }
  .canvas { position: relative; width: 1200px; height: 1000px; }

  .card {
    position: absolute; left: 250px; width: 700px; height: 400px;
    overflow: hidden; box-shadow: 0 10px 30px rgba(0,0,0,.45);
  }

  /* Front */
  .card-front {
    top: 70px;
    background: radial-gradient(ellipse at 50% 30%, var(--card-black-soft), var(--card-black) 75%);
    display: flex; align-items: center; justify-content: center;
  }
  .brand-name {
    color: var(--silver); font-weight: 600; font-size: 44px;
    letter-spacing: 1px; text-transform: uppercase; text-align: center; line-height: 1.15;
  }

  /* Back */
  .card-back { top: 530px; background: var(--card-black); }
  .back-band {
    position: absolute; left: 0; top: 0; width: 100%; height: 165px;
    background: var(--paper);
  }
  .back-brand {
    position: absolute; left: 44px; bottom: 22px;
    color: var(--ink); font-weight: 600; font-size: 36px; letter-spacing: .5px;
  }
  .holder { position: absolute; left: 44px; top: 190px; color: var(--paper); }
  .holder-name { font-size: 24px; font-weight: 500; letter-spacing: 1px; text-transform: uppercase; }
  .holder-title { font-size: 17px; color: var(--muted); margin-top: 2px; }

  .contact-list, .social-list { position: absolute; list-style: none; color: var(--paper); font-size: 15px; }
  .contact-list { left: 44px; bottom: 34px; }
  .social-list { right: 44px; top: 190px; }
  .contact-list li, .social-list li { display: flex; align-items: center; gap: 8px; line-height: 24px; }
  .icon { width: 14px; height: 14px; flex: none; }
  .social-dot { width: 12px; height: 12px; border-radius: 50%; border: 1.5px solid var(--paper); flex: none; }
</style>
</head>
<body>
<main class="canvas">

  <section class="card card-front" aria-label="Card front">
    <div class="brand-name">Quiet Harbor<br>Podcast</div>
  </section>

  <section class="card card-back" aria-label="Card back">
    <div class="back-band">
      <div class="back-brand">Quiet Harbor</div>
    </div>

    <div class="holder">
      <div class="holder-name">Teodor Vask</div>
      <div class="holder-title">Creator/Host</div>
    </div>

    <ul class="social-list">
      <li><span class="social-dot"></span>@qharborcast</li>
      <li><span class="social-dot"></span>@quietharborcastshow</li>
      <li><span class="social-dot"></span>Quiet Harbor Podcast</li>
    </ul>

    <ul class="contact-list">
      <li>
        <svg class="icon" viewBox="0 0 16 16" fill="none" stroke="#fff" stroke-width="1.3"><rect x="1.5" y="3.5" width="13" height="9"/><path d="M1.5 3.5 8 9l6.5-5.5"/></svg>
        teodor@quietharborcast.com
      </li>
      <li>
        <svg class="icon" viewBox="0 0 16 16" fill="none" stroke="#fff" stroke-width="1.3"><circle cx="8" cy="8" r="6.5"/><path d="M5.5 4.5l1.5 1.5-1 1c.5 1.2 1.3 2 2.5 2.5l1-1 1.5 1.5-1 1c-2.5-.3-4.7-2.5-5-5z"/></svg>
        (555) 274-9163
      </li>
      <li>
        <svg class="icon" viewBox="0 0 16 16" fill="none" stroke="#fff" stroke-width="1.3"><circle cx="8" cy="8" r="6.5"/><ellipse cx="8" cy="8" rx="3" ry="6.5"/><path d="M1.5 8h13"/></svg>
        www.quietharborcast.com
      </li>
    </ul>
  </section>

</main>
</body>
</html>
```